We need a full corporate logo and stationary design for our business oxForge. OxForge provides 3D Printing Services to the Australian Market.

Our predominant market is the Mining and Architectural industries and our secondary market is the Entrepreneur / Start-up sector.

What we are after:

1. Logo
2. Business Card Design
3. Letterhead Design
4. Email Signature Design

File Formats we require in colour, greyscale and Black and White:

1 .AI
2 .EPS
3 .TIF
4 .PDF
5 .PNG (300 dpi)
6 .JPG (300 dpi)
7 .GIF (300 dpi)

• Should Not Have:
- "Clip-Art" should not be used.

```html
<!DOCTYPE html>
<html lang="en">
<head>
<meta charset="utf-8">
<title>oxForge Business Card</title>
<link href="https://fonts.googleapis.com/css2?family=Open+Sans:wght@400;600;700&display=swap" rel="stylesheet">
<style>
  :root {
    --stage: #231f20;
    --deep-violet: #3c3f98;
    --royal-blue: #1e6fc0;
    --bright-cyan: #0aaae8;
    --sky-cyan: #00b4f0;
    --paper: #ffffff;
    --ink: #2a2a2a;
  }
  html, body {
    margin: 0;
    padding: 0;
    width: 1144px;
    height: 1200px;
    overflow: hidden;
    background: var(--stage);
  }
  .stage {
    position: relative;
    width: 1144px;
    height: 1200px;
    background: var(--stage);
    font-family: "Open Sans", Arial, sans-serif;
  }
  .card {
    position: absolute;
    left: 166px;
    width: 812px;
    height: 464px;
    overflow: hidden;
  }
  .card-front { top: 98px; }
  .card-back { top: 637px; }
  .card svg { display: block; width: 100%; height: 100%; }
  .name { font-size: 30px; font-weight: 400; fill: var(--paper); }
  .role { font-size: 20px; font-weight: 400; fill: var(--paper); }
  .contact { font-size: 18px; font-weight: 400; fill: var(--paper); }
  .contact-email { font-size: 20px; }
  .wordmark { font-size: 60px; font-weight: 600; fill: var(--ink); letter-spacing: -1px; }
  .website { font-size: 20px; font-weight: 700; fill: var(--paper); }
</style>
</head>
<body>
<div class="stage">

  <section class="card card-front" aria-label="Business card front">
    <svg viewBox="0 0 875 500" xmlns="http://www.w3.org/2000/svg">
      <defs>
        <radialGradient id="frontSky" cx="0.62" cy="0.5" r="0.75">
          <stop offset="0" stop-color="var(--bright-cyan)"/>
          <stop offset="0.6" stop-color="var(--royal-blue)"/>
          <stop offset="1" stop-color="var(--deep-violet)"/>
        </radialGradient>
        <linearGradient id="frontBand" x1="0" y1="0" x2="1" y2="0">
          <stop offset="0" stop-color="var(--sky-cyan)"/>
          <stop offset="0.55" stop-color="var(--bright-cyan)"/>
          <stop offset="1" stop-color="var(--deep-violet)"/>
        </linearGradient>
        <linearGradient id="mapFill" x1="0" y1="0" x2="0" y2="1">
          <stop offset="0" stop-color="#1a8ad6"/>
          <stop offset="1" stop-color="var(--deep-violet)"/>
        </linearGradient>
      </defs>
      <rect class="sky" width="875" height="500" fill="url(#frontSky)"/>
      <polygon class="accent-band" points="0,155 820,362 875,375 0,205" fill="url(#frontBand)"/>
      <polygon class="paper-panel" points="0,205 875,375 875,500 0,500" fill="var(--paper)"/>

      <rect class="map-area" x="12" y="242" width="256" height="180" rx="30" fill="url(#mapFill)"
            role="img" aria-label="Map of Australia"/>

      <text class="name" x="47" y="108">your name</text>
      <text class="role" x="47" y="132">ceo</text>

      <g class="contact-block" text-anchor="end">
        <text class="contact" x="782" y="107">Address, street hgfg 789</text>
        <text class="contact" x="782" y="129">jhjhgjhh jgjhgjh g</text>
        <text class="contact" x="782" y="182">(office) - (20) 123 4567 899</text>
        <text class="contact" x="782" y="204">(mobile) - (20) 123 4567 899</text>
        <text class="contact contact-email" x="782" y="254">yournameceo@oxforge.com</text>
      </g>

      <g class="icon-pin" fill="var(--paper)">
        <path d="M806 82 a17 17 0 0 1 17 17 c0 14 -17 44 -17 44 s-17 -30 -17 -44 a17 17 0 0 1 17 -17z"/>
        <circle cx="806" cy="99" r="6" fill="#1a7ccc"/>
      </g>
      <g class="icon-phone" fill="none" stroke="var(--paper)" stroke-width="3">
        <rect x="793" y="162" width="28" height="51" rx="4"/>
        <line x1="797" y1="205" x2="817" y2="205"/>
      </g>
      <g class="icon-mail" fill="none" stroke="var(--paper)" stroke-width="2.5">
        <rect x="786" y="231" width="41" height="28" fill="var(--paper)"/>
        <polyline points="786,231 806,248 827,231" stroke="#1a7ccc"/>
      </g>

      <text class="wordmark" x="2" y="480">oxForge Australia</text>
    </svg>
  </section>

  <section class="card card-back" aria-label="Business card back">
    <svg viewBox="0 0 875 500" xmlns="http://www.w3.org/2000/svg">
      <defs>
        <radialGradient id="backSky" cx="0.5" cy="0.5" r="0.72">
          <stop offset="0" stop-color="var(--bright-cyan)"/>
          <stop offset="0.65" stop-color="var(--royal-blue)"/>
          <stop offset="1" stop-color="var(--deep-violet)"/>
        </radialGradient>
        <linearGradient id="backBand" x1="0" y1="0" x2="1" y2="0">
          <stop offset="0" stop-color="var(--sky-cyan)"/>
          <stop offset="0.6" stop-color="var(--bright-cyan)"/>
          <stop offset="1" stop-color="var(--deep-violet)"/>
        </linearGradient>
      </defs>
      <rect class="sky" width="875" height="500" fill="url(#backSky)"/>
      <polygon class="accent-band" points="0,155 875,375 0,205" fill="url(#backBand)"/>
      <polygon class="lower-panel" points="0,205 875,375 875,500 0,500" fill="#0f93da" opacity="0.55"/>

      <rect class="map-area" x="241" y="82" width="395" height="337" rx="40" fill="var(--paper)"
            role="img" aria-label="Map of Australia"/>

      <text class="website" x="437" y="448" text-anchor="middle">www.oxforge.com</text>
    </svg>
  </section>

</div>
</body>
</html>
```